Project RUL

I am setting up a consultancy company in Istanbul, Turkey called RUL Partners. RUL partners will focus areas are highlighted in the attached presenatation. Expertise area as follows; Corporate Communications, Digitilization and Technology Integration, CSR & Sponsorships, Investor Relations and Fİnancial PR, Strategic Transactions, Corporate Governance... In related arease Project Management and Training support given.. For details see presenations. Our company collars are marun and blue.. In the attached presenations you can also see the business card colars and logo design. The design should reflect innovationi technology knowhow and power of communications skills. Enclosed you can find a presentations of scope of consultancy services and corporate logo from which logo and colars can be adapted..

Target Market(s)

Potential clients are any Holding or Company that would need services defined in the presantation attached.

Industry/Entity Type

It Company

Coding

Coded - Design and coding required

Number of Pages Required

5+ page

Font styles to use
Sans Serif

Requirements
Must have
• Main Expertize areas are defined in the presentation. The clients should be able to clearly see these and as they select the related area go to related page to see the content detail. I should be to also include vision statement in front page.. I should be able to present partners of the company in a related section. site should allow posting of pictures and an introductory video... Please use the logo and colars ı provided on attached file. Marun should be the dominating colar.
Nice to have
• www.thorvick.example I like.. Thorvick provides somewhat similar services world wide. You can check out the site but don't need to necessarly do the same..

```html
<!DOCTYPE html>
<html lang="en">
<head>
<meta charset="utf-8">
<title>RUL Partners</title>
<link rel="stylesheet" href="https://fonts.googleapis.com/css2?family=Oswald:wght@400&family=Roboto:ital,wght@0,300;0,400;0,500;1,300&display=swap">
<style>
:root{
  --maroon:#6c0f58;
  --maroon-dark:#5a0b49;
  --blue:#2b2a8f;
  --ink:#333333;
  --muted:#8a8a8a;
  --rule:#dddddd;
  --band:#f2f2f2;
  --white:#ffffff;
}
*{margin:0;padding:0;box-sizing:border-box}
html,body{width:1200px;height:2400px;overflow:hidden;background:var(--white)}
body{position:relative;font-family:"Roboto",Arial,sans-serif;color:var(--ink)}
.abs{position:absolute}

/* header */
.site-header{position:absolute;left:0;top:0;width:1200px;height:116px;background:var(--white)}
.brand{position:absolute;left:85px;top:38px;font-size:34px;font-weight:500;color:var(--blue);letter-spacing:1px;font-family:"Roboto",Arial,sans-serif}
.main-nav{position:absolute;left:344px;top:76px;display:flex;gap:31px;font-size:12px;color:#777;text-transform:uppercase}
.main-nav .active{color:var(--maroon);border-bottom:2px solid var(--maroon);padding-bottom:5px}
.social-top{position:absolute;left:984px;top:21px;display:flex;gap:6px}
.social-top span{width:28px;height:28px;border-radius:50%;background:#d9d9d9;display:block}
.search{position:absolute;left:920px;top:70px;width:190px;height:26px;border:1px solid #d5d5d5;font-size:11px;color:#bbb;padding:6px 9px}
.search svg{position:absolute;right:7px;top:6px}

/* hero */
.hero{position:absolute;left:0;top:117px;width:1200px;height:541px;background:linear-gradient(100deg,#1a1a1c 0%,#2c2a2a 30%,#8a6250 55%,#5d4034 68%,#111 82%,#0c0c0c 100%)}
.hero-panel{position:absolute;left:64px;top:157px;width:611px;height:384px;background:rgba(255,255,255,.1)}
.hero-title{position:absolute;left:99px;top:318px;font-family:"Oswald",Arial,sans-serif;font-size:48px;color:var(--white);line-height:1}
.hero-text{position:absolute;left:99px;top:384px;width:540px;font-size:14px;line-height:20px;color:#eee}
.btn{position:absolute;display:flex;align-items:center;justify-content:center;gap:12px;color:var(--white);font-size:13px;text-transform:uppercase}
.btn-blue{left:99px;top:464px;width:147px;height:35px;background:var(--blue)}
.hero-arrows{position:absolute;left:99px;top:533px;display:flex;gap:10px}
.hero-arrows span{width:24px;height:22px;border:1px solid #fff;display:flex;align-items:center;justify-content:center}

/* vision */
.section-title{font-weight:300;font-size:42px;color:var(--ink);line-height:1}
.vision-title{position:absolute;left:86px;top:728px}
.vision-text{position:absolute;left:86px;top:786px;width:520px;font-size:13px;line-height:20.5px;color:var(--muted)}
.vision-text p+p{margin-top:20px}
.btn-maroon{left:86px;top:992px;width:154px;height:35px;background:var(--maroon)}
.video{position:absolute;left:675px;top:731px;width:437px;height:306px;background:linear-gradient(135deg,#6d6d70,#4b4b4e 55%,#5e5a58)}
.video-play{position:absolute;left:183px;top:101px}
.video-bar{position:absolute;left:0;bottom:0;width:437px;height:22px;background:#1c1c1c;color:#bbb;font-size:9px;padding:6px 76px}

/* centered heading with rules */
.rule-heading{position:absolute;left:0;width:1200px;display:flex;align-items:center;gap:24px}
.rule-heading::before,.rule-heading::after{content:"";flex:1;height:1px;background:var(--rule)}

/* expertise */
.card{position:absolute;width:293px}
.card-img{width:293px;height:149px}
.card-title{margin-top:24px;font-size:13px;color:var(--maroon);text-transform:uppercase;padding-bottom:8px;border-bottom:1px solid var(--rule)}
.card-text{margin-top:10px;font-size:10.5px;line-height:14px;color:var(--muted)}
.card-more{margin-top:10px;font-size:9px;color:#555;text-transform:uppercase}

/* testimonials */
.avatar{position:absolute;left:182px;top:1920px;width:128px;height:128px;border-radius:50%;border:6px solid #f0f0f0;box-shadow:0 0 0 1px #e2e2e2;background:linear-gradient(160deg,#e9e9e9,#c9c9cc)}
.quote-mark{position:absolute;left:352px;top:1914px;font-size:28px;color:#bbb;font-family:Georgia,serif}
.quote{position:absolute;left:374px;top:1930px;width:630px;font-size:13px;line-height:20.5px;font-style:italic;font-weight:300;color:#555}
.quote-author{position:absolute;left:368px;top:2002px;font-size:13px;color:#555}
.quote-arrows{position:absolute;left:368px;top:2052px;display:flex;gap:14px}

/* partners band */
.partners{position:absolute;left:0;top:2115px;width:1200px;height:157px;background:var(--band)}
.partner-badge{position:absolute;top:58px;height:40px;background:#c4c4c4;border-radius:4px}

/* footer */
.site-footer{position:absolute;left:0;top:2272px;width:1200px;height:128px;background:var(--maroon-dark)}
.footer-links{position:absolute;left:0;top:45px;width:1200px;text-align:center;font-size:10.5px;color:var(--white);text-transform:uppercase}
.footer-copy{position:absolute;left:0;top:76px;width:1200px;text-align:center;font-size:10px;color:var(--white);text-transform:uppercase}
.social-foot{position:absolute;left:929px;top:49px;display:flex;gap:7px}
.social-foot span{width:40px;height:40px;border-radius:50%;background:#84276f;display:block}
</style>
</head>
<body>

<header class="site-header">
  <div class="brand">RUL partners</div>
  <nav class="main-nav">
    <span class="active">Home</span><span>About us</span><span>What we do</span><span>Our expertise</span><span>Testimonials</span><span>Contact</span>
  </nav>
  <div class="social-top"><span></span><span></span><span></span><span></span></div>
  <div class="search">Search
    <svg width="12" height="12" viewBox="0 0 12 12"><circle cx="5" cy="5" r="3.8" fill="none" stroke="#aaa" stroke-width="1.4"/><line x1="8" y1="8" x2="11" y2="11" stroke="#aaa" stroke-width="1.4"/></svg>
  </div>
</header>

<section class="hero" role="img" aria-label="Close-up of two business people in suits shaking hands">
</section>
<div class="hero-panel"></div>
<h1 class="hero-title">RUL Partners</h1>
<p class="hero-text">Lorem ipsum dolor sit amet, consectetur adipisicing elit, sed do eiusmod tempor incididunt ut labore et dolore magna aliqua.Lorem ipsum dolor sit amet, consectetur adipisicing elit, sed do eiusmod tempor incididunt ut labore et dolore magna aliqua.</p>
<div class="btn btn-blue">Know more
  <svg width="8" height="11" viewBox="0 0 8 11"><path d="M1.5 1l5 4.5-5 4.5" fill="none" stroke="#fff" stroke-width="2"/></svg>
</div>
<div class="hero-arrows">
  <span><svg width="7" height="10" viewBox="0 0 7 10"><path d="M6 1L2 5l4 4" fill="none" stroke="#fff" stroke-width="1.6"/></svg></span>
  <span><svg width="7" height="10" viewBox="0 0 7 10"><path d="M1 1l4 4-4 4" fill="none" stroke="#fff" stroke-width="1.6"/></svg></span>
</div>

<section>
  <h2 class="section-title vision-title">Our Vision</h2>
  <div class="vision-text">
    <p>Lorem ipsum dolor sit amet, consectetur adipisicing elit, sed do eiusmod tempor incididunt ut labore et dolore magna aliqua. Ut enim ad minim veniam, quis nostrud exercitation ullamco laboris nisi ut aliquip ex ea commodo consequat. Duis aute irure dolor in reprehenderit in voluptate velit esse cillum dolore eu fugiat nulla pariatur. Lorem ipsum dolor sit amet, consectetur adipisicing elit, sed do eiusmod tempor incididunt ut labore et dolore magna aliqua.</p>
    <p>Ut enim ad minim veniam, quis nostrud exercitation ullamco laboris nisi ut aliquip ex ea commodo consequat.</p>
  </div>
  <div class="btn btn-maroon">Read more
    <svg width="8" height="11" viewBox="0 0 8 11"><path d="M1.5 1l5 4.5-5 4.5" fill="none" stroke="#fff" stroke-width="2"/></svg>
  </div>
  <div class="video" role="img" aria-label="Introductory video still of consultants in a meeting">
    <svg class="video-play" width="70" height="70" viewBox="0 0 70 70"><circle cx="35" cy="35" r="32" fill="rgba(0,0,0,.25)" stroke="#fff" stroke-width="3"/><path d="M27 20l22 15-22 15z" fill="#fff"/></svg>
    <div class="video-bar">0:00 / 2:01</div>
  </div>
</section>

<section>
  <h2 class="rule-heading section-title" style="top:1110px">Our Expertise Area</h2>

  <article class="card" style="left:123px;top:1197px">
    <div class="card-img" role="img" aria-label="Hands holding a tablet and a smartphone" style="background:linear-gradient(120deg,#3b2c22,#9a7a5c 50%,#e09a3a)"></div>
    <h3 class="card-title">Corporate Communications</h3>
    <p class="card-text">Ut enim ad minim veniam, quis nostrud exercitation ullamco laboris nisi ut aliquip ex ea commodo consequat.</p>
    <p class="card-more">[ Read more ]</p>
  </article>
  <article class="card" style="left:453px;top:1197px">
    <div class="card-img" role="img" aria-label="Finger touching a glowing digital network interface" style="background:linear-gradient(135deg,#0c2440,#1d6fa0 55%,#0b1e36)"></div>
    <h3 class="card-title">Digitilization and Technology Integration</h3>
    <p class="card-text">Ut enim ad minim veniam, quis nostrud exercitation ullamco laboris nisi ut aliquip ex ea commodo consequat.</p>
    <p class="card-more">[ Read more ]</p>
  </article>
  <article class="card" style="left:781px;top:1197px">
    <div class="card-img" role="img" aria-label="Business partners shaking hands over a meeting table" style="background:linear-gradient(135deg,#3a3d44,#c9ccd0 55%,#8e939a)"></div>
    <h3 class="card-title">CSR &amp; Sponsorships</h3>
    <p class="card-text">Ut enim ad minim veniam, quis nostrud exercitation ullamco laboris nisi ut aliquip ex ea commodo consequat.</p>
    <p class="card-more">[ Read more ]</p>
  </article>

  <article class="card" style="left:123px;top:1507px">
    <div class="card-img" role="img" aria-label="Businessman stacking gold coins" style="background:linear-gradient(135deg,#56585e,#8b7a55 55%,#c7b27a)"></div>
    <h3 class="card-title">Investor Relations and Fİnancial PR</h3>
    <p class="card-text">Ut enim ad minim veniam, quis nostrud exercitation ullamco laboris nisi ut aliquip ex ea commodo consequat.</p>
    <p class="card-more">[ Read more ]</p>
  </article>
  <article class="card" style="left:453px;top:1507px">
    <div class="card-img" role="img" aria-label="Golden rising bar graph" style="background:linear-gradient(135deg,#f6e3a0,#d7a33a 55%,#f3d98a)"></div>
    <h3 class="card-title">Strategic Transactions</h3>
    <p class="card-text">Ut enim ad minim veniam, quis nostrud exercitation ullamco laboris nisi ut aliquip ex ea commodo consequat.</p>
    <p class="card-more">[ Read more ]</p>
  </article>
  <article class="card" style="left:781px;top:1507px">
    <div class="card-img" role="img" aria-label="Empty boardroom with a long polished table" style="background:linear-gradient(180deg,#d9a572,#a4552a 55%,#6d2c17)"></div>
    <h3 class="card-title">Corporate Governance</h3>
    <p class="card-text">Ut enim ad minim veniam, quis nostrud exercitation ullamco laboris nisi ut aliquip ex ea commodo consequat.</p>
    <p class="card-more">[ Read more ]</p>
  </article>
</section>

<section>
  <h2 class="rule-heading section-title" style="top:1846px">Testimonials</h2>
  <div class="avatar" role="img" aria-label="Portrait photo of the client giving the testimonial"></div>
  <span class="quote-mark">&ldquo;</span>
  <p class="quote">Lorem ipsum dolor sit amet, consectetur adipisicing elit, sed do eiusmod tempor incididunt ut labore et dolore magna aliqua. Ut enim ad minim veniam, quis nostrud exercitation ullamco laboris nisi ut aliquip ex ea commodo consequat. Duis aute irure dolor in reprehenderit in voluptate velit esse cillum pariatur.</p>
  <p class="quote-author">- Delan Morrow</p>
  <div class="quote-arrows">
    <svg width="10" height="16" viewBox="0 0 10 16"><path d="M8 2L3 8l5 6" fill="none" stroke="#bbb" stroke-width="2"/></svg>
    <svg width="10" height="16" viewBox="0 0 10 16"><path d="M2 2l5 6-5 6" fill="none" stroke="#bbb" stroke-width="2"/></svg>
  </div>
</section>

<section class="partners" aria-label="Technology partners">
  <div class="partner-badge" style="left:108px;width:108px"></div>
  <div class="partner-badge" style="left:246px;width:78px;border-radius:20px"></div>
  <div class="partner-badge" style="left:374px;width:88px;border-radius:0"></div>
  <div class="partner-badge" style="left:503px;width:80px"></div>
  <div class="partner-badge" style="left:626px;width:80px;border-radius:20px"></div>
  <div class="partner-badge" style="left:738px;width:110px"></div>
  <div class="partner-badge" style="left:896px;width:44px;height:52px;top:52px;border-radius:0"></div>
  <div class="partner-badge" style="left:992px;width:106px"></div>
</section>

<footer class="site-footer">
  <p class="footer-links">Home &nbsp;|&nbsp; About us &nbsp;|&nbsp; What we do &nbsp;|&nbsp; Expertise &nbsp;|&nbsp; Testimonials &nbsp;|&nbsp; Contact</p>
  <p class="footer-copy">All rights reserved. Copyrights @ 2014</p>
  <div class="social-foot"><span></span><span></span><span></span><span></span></div>
</footer>

</body>
</html>
```